Brochure & Flyer Design

Coral Skipper Elmgrove - Fish & Chips is a popular fish and chip store located on Sydney’s beautiful northern beaches. It sits just across from the sandy shores of Newport Beach.
Please see attached:
1. Details on the brochure I would like designed for Coral Skipper Elmgrove
2. Current menu that is in store that will need to be included
3. Logo
I would like a modern, fresh design to complement the logo focusing on the food.
Here is the link to download the images that should be included in the brochure https://www.filedrift.net/fetch/PxKmTzQaVbRnLwYcJdHsKe
To complement the brochure I would like an A1 flyer template that can be used to promote specials at the store.

```html
<!DOCTYPE html>
<html lang="en">
<head>
<meta charset="utf-8">
<title>Coral Skipper Elmgrove - Fish &amp; Chips | Menu Back Side</title>
<link href="https://fonts.googleapis.com/css2?family=Kaushan+Script&family=Didact+Gothic&display=swap" rel="stylesheet">
<style>
  :root {
    --page-bg: #ece8e3;
    --blue-deep: #1a56a3;
    --blue-mid: #2a76c0;
    --blue-light: #4aa3da;
    --navy: #1f2f62;
    --white: #ffffff;
    --yellow: #f6e323;
    --orange: #ef7d22;
    --card-line: #b9c2cf;
    --photo-warm: #d9a55a;
    --photo-cool: #c8d3df;
  }
  * { box-sizing: border-box; margin: 0; padding: 0; }
  html, body { width: 1200px; height: 1000px; overflow: hidden; }
  body {
    background: var(--page-bg);
    font-family: "Didact Gothic", "Century Gothic", sans-serif;
    position: relative;
  }
  .brochure {
    position: absolute; left: 56px; top: 190px; width: 1087px; height: 770px;
    display: flex; box-shadow: 0 4px 14px rgba(0,0,0,.35);
  }
  .panel {
    position: relative; height: 100%;
    background: radial-gradient(ellipse at 50% 8%, var(--blue-light) 0%, var(--blue-mid) 40%, var(--blue-deep) 100%);
  }
  .panel + .panel { border-left: 1px solid rgba(0,0,0,.18); }
  .panel--pack { width: 360px; }
  .panel--burgers { width: 366px; }
  .panel--individual { width: 361px; }

  .section-tag {
    position: absolute; height: 66px; background: var(--white);
    border-radius: 0 0 6px 6px; box-shadow: 0 3px 6px rgba(0,0,0,.3);
    display: flex; align-items: center; justify-content: center; gap: 10px;
  }
  .section-tag::before {
    content: ""; position: absolute; inset: 5px; border: 1px solid var(--card-line); border-radius: 4px;
  }
  .section-tag__rule { width: 26px; height: 2px; background: var(--orange); border-radius: 2px; }
  .section-tag__title {
    font-family: "Kaushan Script", cursive; font-size: 27px; color: var(--navy);
  }

  .price-list { position: absolute; left: 27px; top: 108px; width: 230px; list-style: none; }
  .price-list li {
    height: 25.8px; color: var(--white); font-size: 16px; display: flex; overflow: hidden; white-space: nowrap;
  }
  .price-list li::after { content: "................................................"; letter-spacing: 1px; opacity: .9; }
  .price-column {
    position: absolute; left: 272px; top: 92px; width: 72px; height: 386px;
    background: var(--white); border-radius: 10px; padding-top: 10px;
    list-style: none; box-shadow: 0 2px 4px rgba(0,0,0,.25);
  }
  .price-column li { height: 25.8px; text-align: center; color: var(--orange); font-size: 17px; }
  sup { font-size: 11px; vertical-align: 6px; }

  .meal { position: absolute; color: var(--white); font-size: 13px; line-height: 16px; }
  .meal__name { color: var(--yellow); font-style: italic; font-size: 17px; line-height: 20px; }
  .price-chip {
    position: absolute; height: 34px; background: var(--white); border-radius: 4px;
    border: 1px solid var(--card-line); box-shadow: 0 2px 4px rgba(0,0,0,.3);
    color: var(--orange); font-size: 20px; display: flex; align-items: center; justify-content: center;
  }
  .grilled { position: absolute; color: var(--yellow); font-style: italic; font-size: 18px; }

  .combo {
    position: absolute; left: 27px; top: 395px; width: 318px; height: 87px;
    border: 2px solid var(--yellow); text-align: center; color: var(--white);
  }
  .combo__tag {
    position: absolute; left: 68px; top: -24px; width: 176px; height: 46px;
    background: var(--blue-mid); border: 2px solid var(--yellow); border-radius: 4px;
    font-family: "Kaushan Script", cursive; font-size: 22px; color: var(--white);
    display: flex; align-items: center; justify-content: center;
  }
  .combo__text { margin-top: 32px; font-size: 12.5px; font-style: italic; }
  .combo__price { color: var(--yellow); font-size: 21px; margin-top: 4px; }

  .photo { position: absolute; background: linear-gradient(160deg, var(--photo-cool), var(--photo-warm)); }
  .photo--burger { border-radius: 50% 50% 40% 40%; background: radial-gradient(ellipse, #e7a34d 0%, #c77e2e 55%, #8e5a2a 100%); }
  .photo--pack { left: 24px; width: 131px; height: 103px; border: 3px solid var(--white); box-shadow: 0 2px 4px rgba(0,0,0,.3); }
  .burger-label { position: absolute; color: var(--white); text-align: center; }
  .burger-label__name { font-family: "Kaushan Script", cursive; font-size: 18px; }
  .burger-label__price { font-size: 22px; }
  .arrow { position: absolute; overflow: visible; }
</style>
</head>
<body>
<main class="brochure">

  <section class="panel panel--pack">
    <div class="section-tag" style="left:44px;top:0;width:272px;">
      <span class="section-tag__rule"></span><h2 class="section-tag__title">Create a Pack</h2><span class="section-tag__rule"></span>
    </div>
    <ul class="price-list">
      <li>Fillet of Fish</li><li>Fish Cocktail</li><li>Calamiri Ring</li><li>Prawn Cutlet</li>
      <li>Sea Scallop</li><li>Ocean Mussel</li><li>Seafood Stick</li><li>Small Chips</li>
      <li>Large Chips</li><li>Potato Scallop</li><li>Banana Fritter</li><li>Pineapple Fritter</li>
      <li>Vegie Spring Roll</li><li>Extra Sauce</li>
    </ul>
    <ul class="price-column">
      <li><sup>$</sup>8.90</li><li><sup>$</sup>2.40</li><li><sup>$</sup>1.00</li><li><sup>$</sup>2.40</li>
      <li><sup>$</sup>2.40</li><li><sup>$</sup>1.00</li><li><sup>$</sup>1.80</li><li><sup>$</sup>4.50</li>
      <li><sup>$</sup>7.00</li><li><sup>$</sup>1.00</li><li><sup>$</sup>3.00</li><li><sup>$</sup>3.00</li>
      <li><sup>$</sup>2.50</li><li>50<sup>c</sup></li>
    </ul>

    <div class="section-tag" style="left:46px;top:505px;width:270px;border-radius:6px;">
      <span class="section-tag__rule"></span><h2 class="section-tag__title">Family Meals</h2><span class="section-tag__rule"></span>
    </div>
    <div class="meal" style="left:29px;top:586px;width:230px;">
      <h3 class="meal__name">Fishermans Basket</h3>
      <p>2 Fillet of Fish, 6 Calamary Rings, 4 Pawns, 4 Sea Scallops, Large Chips, Lemon &amp; Sauce</p>
    </div>
    <div class="price-chip" style="left:266px;top:611px;width:84px;"><sup>$</sup>39.90</div>
    <div class="meal" style="left:29px;top:673px;width:240px;">
      <h3 class="meal__name">Dinner Pack</h3>
      <p>4 Fillets of Fish, 12 Calamary Rings, Large Chips, Lemon &amp; Sauce</p>
    </div>
    <div class="price-chip" style="left:266px;top:699px;width:84px;"><sup>$</sup>42.90</div>
  </section>

  <section class="panel panel--burgers">
    <div class="section-tag" style="left:48px;top:0;width:272px;">
      <span class="section-tag__rule"></span><h2 class="section-tag__title">Burgers</h2><span class="section-tag__rule"></span>
    </div>
    <div class="meal" style="left:27px;top:110px;width:210px;">
      <h3 class="meal__name">Outrigger Burger</h3><p>4 Calamari Rings, Garden Lettuce &amp; Tartare Sauce</p>
    </div>
    <div class="price-chip" style="left:270px;top:128px;width:75px;"><sup>$</sup>7.90</div>
    <div class="meal" style="left:27px;top:183px;width:210px;">
      <h3 class="meal__name">Odessey Burger</h3><p>Fish Fillet, Coleslaw Salad &amp; Seafood Sauce</p>
    </div>
    <div class="price-chip" style="left:270px;top:201px;width:75px;"><sup>$</sup>7.90</div>
    <div class="meal" style="left:27px;top:256px;width:210px;">
      <h3 class="meal__name">Olympiad Burger</h3><p>Fish Fillet, Fresh Tomato, Garden Lettuce &amp; Tartare Sauce</p>
    </div>
    <div class="price-chip" style="left:270px;top:274px;width:75px;"><sup>$</sup>7.90</div>
    <p class="grilled" style="left:27px;top:328px;">Grilled + $2</p>

    <div class="combo">
      <h2 class="combo__tag">Burger Combo</h2>
      <p class="combo__text">Choose any burger with chips and 600ml water</p>
      <p class="combo__price"><sup>$</sup>12.90</p>
    </div>

    <div class="photo photo--burger" role="img" aria-label="Photo of the Odessey fish burger" style="left:26px;top:505px;width:138px;height:105px;"></div>
    <svg class="arrow" style="left:160px;top:510px;" width="50" height="20" viewBox="0 0 50 20"><path d="M2 8 Q24 -2 46 10" fill="none" stroke="#fff" stroke-width="1.5"/><path d="M40 5 L46 10 L39 13" fill="none" stroke="#fff" stroke-width="1.5"/></svg>
    <div class="burger-label" style="left:200px;top:520px;width:140px;">
      <p class="burger-label__name">Odessey Burger</p><p class="burger-label__price">$ 7.90</p>
    </div>

    <div class="photo photo--burger" role="img" aria-label="Photo of the Olympiad fish burger" style="left:210px;top:635px;width:125px;height:100px;"></div>
    <svg class="arrow" style="left:168px;top:645px;" width="50" height="20" viewBox="0 0 50 20"><path d="M48 4 Q26 -2 4 12" fill="none" stroke="#fff" stroke-width="1.5"/><path d="M10 6 L4 12 L11 14" fill="none" stroke="#fff" stroke-width="1.5"/></svg>
    <div class="burger-label" style="left:22px;top:665px;width:150px;">
      <p class="burger-label__name">Olympiad Burger</p><p class="burger-label__price">$ 7.90</p>
    </div>
  </section>

  <section class="panel panel--individual">
    <div class="section-tag" style="left:45px;top:0;width:270px;">
      <span class="section-tag__rule"></span><h2 class="section-tag__title">Individual</h2><span class="section-tag__rule"></span>
    </div>

    <div class="photo photo--pack" role="img" aria-label="Photo of fish cocktails and chips in a takeaway box" style="top:93px;"></div>
    <div class="meal" style="left:170px;top:98px;width:185px;"><h3 class="meal__name">Fish Cocktail Pack</h3><p>6 Fish Cocktails and Chips</p></div>
    <div class="price-chip" style="left:198px;top:151px;width:75px;"><sup>$</sup>13.90</div>

    <div class="photo photo--pack" role="img" aria-label="Photo of a junior pack with fish, calamari and chips" style="top:205px;"></div>
    <div class="meal" style="left:170px;top:209px;width:185px;"><h3 class="meal__name">Junior Pack</h3><p>2 Fish Cocktails, 2 Calamari Rings, 1 Seafood Stick &amp; Chips</p></div>
    <div class="price-chip" style="left:198px;top:274px;width:75px;"><sup>$</sup>9.90</div>

    <div class="photo photo--pack" role="img" aria-label="Photo of calamari rings and chips with lemon" style="top:317px;"></div>
    <div class="meal" style="left:170px;top:322px;width:185px;"><h3 class="meal__name">Calamari Pack</h3><p>8 Calamari Rings and Chips</p></div>
    <div class="price-chip" style="left:198px;top:375px;width:75px;"><sup>$</sup>11.90</div>

    <div class="photo photo--pack" role="img" aria-label="Photo of a battered fish fillet and chips" style="top:429px;"></div>
    <div class="meal" style="left:170px;top:432px;width:185px;"><h3 class="meal__name">Fish &amp; Chips</h3><p>1 Fillet of Fish and Chips</p><p style="color:var(--yellow);font-style:italic;">Grilled + $2</p></div>
    <div class="price-chip" style="left:198px;top:490px;width:75px;"><sup>$</sup>11.90</div>

    <div class="photo photo--pack" role="img" aria-label="Photo of prawns and chips with lemon" style="top:541px;"></div>
    <div class="meal" style="left:170px;top:545px;width:185px;"><h3 class="meal__name">Prawn Pack</h3><p>6 Prawns and Chips</p></div>
    <div class="price-chip" style="left:198px;top:599px;width:75px;"><sup>$</sup>14.50</div>

    <div class="photo photo--pack" role="img" aria-label="Photo of sea scallops and chips with lemon" style="top:653px;"></div>
    <div class="meal" style="left:170px;top:655px;width:185px;"><h3 class="meal__name">Sea Scallop Pack</h3><p>6 Sea Scallops and Chips</p></div>
    <div class="price-chip" style="left:198px;top:710px;width:75px;"><sup>$</sup>14.50</div>
  </section>

</main>
</body>
</html>
```